Glow With Mirela, Enhancing Your Natural Bauty

Selling lipglosses, adding different types of photos with different colours of lip glosses,adding videos etc

Target Market(s)

All

Industry/Entity Type

Beauty industy

Coding

Coded - Design and coding required

Number of Pages Required

4 page

Requirements
Must have
• All payment options,easy to find,clear photos
Nice to have
• Photos of different ethnicity.Black,asian,white women

```html
<!DOCTYPE html>
<html lang="en">
<head>
<meta charset="utf-8">
<title>Glow With Mirela – Lip Gloss Store</title>
<link href="https://fonts.googleapis.com/css2?family=Playfair+Display:wght@400;600;700&family=Poppins:ital,wght@0,400;0,500;0,600;1,400&display=swap" rel="stylesheet">
<style>
:root{
  --stage:#b6b6bf;
  --pink:#ee6d95;
  --pink-soft:#f285a6;
  --pink-pale:#fdeef2;
  --red:#e8383f;
  --ink:#222226;
  --grey-text:#555;
  --light:#f6f6f6;
  --dark:#2b2b2b;
  --gold:#f5b400;
  --white:#fff;
}
*{box-sizing:border-box;margin:0;padding:0}
html,body{width:1200px;height:1200px;overflow:hidden}
body{background:var(--stage);font-family:'Poppins',sans-serif;color:var(--ink);position:relative}
.serif{font-family:'Playfair Display',serif}
.abs{position:absolute}
.page{position:absolute;background:var(--white);overflow:hidden}
.page-home{left:150px;top:99px;width:427px;height:1028px}
.page-community{left:605px;top:99px;width:428px;height:530px}

/* nav */
.nav{left:0;top:0;width:427px;height:28px;background:rgba(252,232,236,.92);z-index:3}
.nav-logo{left:26px;top:11px;font-family:'Playfair Display',serif;font-size:5px;color:var(--red);letter-spacing:.3px}
.nav-link{top:12px;font-family:'Playfair Display',serif;font-size:3.6px;letter-spacing:1.2px;font-weight:600}
.nav-search{left:370px;top:11px;width:41px;height:8px;border-radius:4px;background:var(--red);color:#fff;font-family:'Playfair Display',serif;font-size:3.4px;letter-spacing:1.2px;text-align:center;line-height:8px}

/* hero */
.hero-photo{left:0;top:0;width:427px;height:264px;background:linear-gradient(100deg,#f09bae 0%,#f4b3bf 40%,#f2d2c6 62%,#e9b7a6 80%,#f1a7b4 100%)}
.hero-box{left:27px;top:75px;width:156px;height:143px;background:rgba(255,255,255,.28)}
.hero-kicker{left:42px;top:92px;font-size:12.5px;font-family:'Playfair Display',serif;font-weight:600;letter-spacing:.3px}
.hero-sale{left:42px;top:107px;font-size:18px;font-family:'Playfair Display',serif;color:var(--red);font-weight:600;letter-spacing:.5px}
.hero-tag{left:42px;top:133px;font-size:10px;font-family:'Playfair Display',serif;font-weight:600;letter-spacing:.3px}
.hero-fine{left:42px;top:149px;width:118px;font-size:2.4px;line-height:3.6px;font-family:'Playfair Display',serif;font-weight:700}
.hero-btn{left:40px;top:170px;width:54px;height:15px;border-radius:8px;background:var(--red);color:#fff;font-family:'Playfair Display',serif;font-size:5px;text-align:center;line-height:15px;letter-spacing:.4px}
.dot{top:219px;width:8px;height:8px;border-radius:50%}

/* intro */
.intro{left:0;top:264px;width:427px;height:209px;background:linear-gradient(110deg,#fdeef2,#fff6f8 60%,#fde8ee)}
.intro-title{left:50px;top:303px;font-family:'Playfair Display',serif;font-weight:700;font-size:16.5px;line-height:19.6px}
.intro-copy{left:50px;top:367px;width:162px;font-size:5.1px;line-height:8px;color:#444}
.btn-solid{background:var(--pink);color:#fff;border-radius:8px;text-align:center;font-size:4.2px;font-weight:500}
.btn-line{border:1px solid var(--pink);color:var(--pink);border-radius:8px;text-align:center;font-size:4.2px;font-weight:500;background:#fff}
.intro-media{left:225px;top:272px;width:172px;height:172px;border-radius:3px;background:linear-gradient(135deg,#f2d7bb,#efceb0 55%,#e9c2a4);box-shadow:0 2px 6px rgba(0,0,0,.08)}
.badge{background:var(--pink);color:#fff;font-size:3.6px;font-weight:500;border-radius:6px;text-align:center}
.play{border-radius:50%;background:rgba(240,120,150,.6)}

/* sale band */
.sale-band{left:0;top:473px;width:427px;height:109px;background:linear-gradient(90deg,#ef7c9e,#f289a8)}
.sale-video{left:7px;top:451px;width:126px;height:71px;background:linear-gradient(90deg,#e8a98f 0%,#ee5d5d 50%,#ef4c4c 100%)}
.sale-title{left:0;top:485px;width:447px;text-align:center;font-family:'Playfair Display',serif;color:#fff;font-size:11px}
.sale-sub{left:0;top:504px;width:447px;text-align:center;color:#fff;font-size:4.5px}
.count{top:520px;height:28px;background:rgba(255,255,255,.22);border-radius:2px;color:#fff;text-align:center}
.count b{display:block;font-size:8.5px;font-weight:600;margin-top:5px;line-height:9px}
.count span{display:block;font-size:2.8px;margin-top:5px;letter-spacing:.2px}
.sale-btn{left:200px;top:556px;width:48px;height:15px;border-radius:8px;background:var(--dark);color:#fff;font-size:4px;text-align:center;line-height:15px;font-weight:500}
.sale-photo{left:289px;top:537px;width:128px;height:72px;background:linear-gradient(135deg,#b3302c,#c2423a 50%,#a92a27)}

/* section heads */
.section-title{width:100%;text-align:center;font-family:'Playfair Display',serif;font-weight:600;color:var(--ink)}
.rule{height:1px;background:var(--pink)}
.section-sub{width:100%;text-align:center;color:#444}

/* categories */
.cat-section{left:0;top:582px;width:427px;height:204px;background:var(--light)}
.card{width:81px;background:#fff;border-radius:3px;box-shadow:0 1px 4px rgba(0,0,0,.08);overflow:hidden}
.card-photo{width:81px}
.cat-name{text-align:center;font-family:'Playfair Display',serif;font-weight:600;font-size:5.5px;margin-top:6px}
.cat-btn{display:block;margin:5px auto 0;width:40px;height:14px;line-height:13px}

/* best sellers */
.prod-name{font-family:'Playfair Display',serif;font-weight:600;font-size:5px;margin:6px 0 0 6px}
.prod-price{margin:3px 0 0 6px;font-size:5px;color:var(--pink);font-weight:600}
.prod-price s{color:#888;font-weight:400;font-size:4.2px;margin-left:2px}
.swatches{display:flex;gap:2.5px;margin:4px 0 0 6px}
.swatches i{width:4.6px;height:4.6px;border-radius:50%;display:block}
.add-btn{margin:3px 0 0 6px;width:42px;height:14px;line-height:14px;display:block}
.tag{top:4px;left:4px;height:7px;padding:0 4px;line-height:7px;font-size:3px;border-radius:4px;background:var(--red);color:#fff}

/* reviews */
.reviews{left:0;top:0;width:428px;height:162px;background:var(--light)}
.review{top:68px;width:110px;height:72px;background:#fff;border-radius:3px;box-shadow:0 1px 4px rgba(0,0,0,.08)}
.avatar{left:7px;top:6px;width:16px;height:16px;border-radius:50%}
.rev-name{left:28px;top:9px;font-family:'Playfair Display',serif;font-weight:600;font-size:4.3px}
.stars{left:28px;top:15px;font-size:5px;color:var(--gold);letter-spacing:.6px}
.quote{left:8px;top:30px;width:96px;font-size:4.1px;line-height:6.9px;font-style:italic;color:#444}

/* instagram */
.insta-tile{top:237px;width:55px;height:54px;border-radius:3px}

/* newsletter */
.newsletter{left:0;top:312px;width:428px;height:95px;background:linear-gradient(110deg,#ef7099,#f390b0)}
.news-title{left:0;top:336px;width:428px;text-align:center;font-family:'Playfair Display',serif;color:#fff;font-size:6.5px;font-weight:600}
.news-copy{left:0;top:351px;width:428px;text-align:center;color:#fff;font-size:4.2px;line-height:7.5px}
.news-input{left:147px;top:373px;width:134px;height:13px;border-radius:7px;background:#fff;overflow:hidden}
.news-input span{position:absolute;left:6px;top:0;line-height:13px;font-size:3.6px;color:#555}
.news-input b{position:absolute;right:0;top:0;width:33px;height:13px;background:var(--dark);color:#fff;font-size:3.4px;line-height:13px;text-align:center;font-weight:500}

/* footer */
.footer{left:0;top:407px;width:428px;height:123px;background:var(--dark);color:#ddd}
.foot-head{top:24px;font-family:'Playfair Display',serif;color:#fff;font-size:5.6px;font-weight:600}
.foot-rule{top:33px;width:11px;height:1px;background:var(--pink)}
.foot-list{top:38px;list-style:none;font-size:4.1px;line-height:10px;color:#ddd}
.foot-about{left:40px;top:38px;width:72px;font-size:4.1px;line-height:6.9px}
.social{top:65px;width:10px;height:10px;border-radius:50%;background:#444}
.social::after{content:"";position:absolute;left:3.3px;top:3.3px;width:3.4px;height:3.4px;border-radius:50%;background:#bbb}
.foot-list svg{width:4px;height:4px;vertical-align:-0.5px;margin-right:1px}
</style>
</head>
<body>

<!-- Home page -->
<main class="page page-home">

  <div class="abs hero-photo" role="img" aria-label="Close-up beauty photo of a model with glossy red lips on a soft pink backdrop"></div>

  <header class="abs nav">
    <div class="abs nav-logo">GLOW WITH MIRELA</div>
    <div class="abs nav-link" style="left:210px">HOME</div>
    <div class="abs nav-link" style="left:258px">SHOP</div>
    <div class="abs nav-link" style="left:309px">PRODUCTS</div>
    <div class="abs nav-search">SEARCH</div>
  </header>

  <div class="abs hero-box"></div>
  <div class="abs hero-kicker">ONLINE EXCLUSIVE</div>
  <div class="abs hero-sale">SALE</div>
  <div class="abs hero-tag">IT’S NOW OR NEVER</div>
  <p class="abs hero-fine">Limited-time savings on glossy, matte and plumping shades. Treat your lips to rich colour and lasting shine today only online.</p>
  <div class="abs hero-btn">SHOP NOW</div>
  <div class="abs dot" style="left:391px;background:#f29bb3"></div>
  <div class="abs dot" style="left:408px;background:#f4b0c0"></div>
  <div class="abs dot" style="left:425px;background:#f5e1e4;display:none"></div>

  <section class="abs intro"></section>
  <h2 class="abs intro-title">Shine Bright with<br>Glow With Mirela<br>Lip Glosses</h2>
  <p class="abs intro-copy">Discover our collection of premium lip glosses that deliver stunning shine, hydration, and color in every swipe. Perfect for every occasion and skin tone.</p>
  <div class="abs btn-solid" style="left:50px;top:400px;width:39px;height:15px;line-height:15px">Shop Now</div>
  <div class="abs btn-line" style="left:95px;top:400px;width:45px;height:15px;line-height:13px">New Arrivals</div>
  <div class="abs intro-media" role="img" aria-label="Video cover: flat lay of makeup brushes, compacts and lipsticks on a peach background"></div>
  <div class="abs badge" style="left:337px;top:278px;width:54px;height:11px;line-height:11px">30% OFF Today Only</div>
  <div class="abs play" style="left:287px;top:325px;width:50px;height:50px"></div>
  <svg class="abs" style="left:305px;top:342px" width="16" height="16" viewBox="0 0 16 16"><path d="M2 1 L15 8 L2 15 Z" fill="#fff"/></svg>

  <section class="abs sale-band"></section>
  <div class="abs sale-video" role="img" aria-label="Video cover: surprised model with red lipstick on a red background"></div>
  <div class="abs play" style="left:66px;top:466px;width:40px;height:40px;background:rgba(255,150,160,.55)"></div>
  <svg class="abs" style="left:80px;top:479px" width="14" height="14" viewBox="0 0 16 16"><path d="M2 1 L15 8 L2 15 Z" fill="#fff"/></svg>
  <h3 class="abs sale-title">Summer Glow Sale</h3>
  <p class="abs sale-sub">Get up to 50% off on our bestselling lip glosses. Limited time offer!</p>
  <div class="abs count" style="left:169px;width:22px"><b>02</b><span>DAYS</span></div>
  <div class="abs count" style="left:196px;width:22px"><b>12</b><span>HOURS</span></div>
  <div class="abs count" style="left:222px;width:26px"><b>45</b><span>MINUTES</span></div>
  <div class="abs count" style="left:252px;width:26px"><b>30</b><span>SECONDS</span></div>
  <div class="abs sale-btn">Shop The Sale</div>

  <section class="abs cat-section"></section>
  <div class="abs sale-photo" role="img" aria-label="Red lipsticks resting on beige makeup sponges over a deep red surface"></div>
  <h2 class="abs section-title" style="left:0;top:604px;font-size:12.5px">Shop By Category</h2>
  <div class="abs rule" style="left:196px;top:625px;width:27px"></div>
  <p class="abs section-sub" style="left:0;top:634px;font-size:4.5px">Find your perfect lip gloss based on your preferences</p>

  <div class="abs card" style="left:50px;top:656px;height:108px">
    <div class="card-photo" style="height:68px;background:linear-gradient(90deg,#e9e9ec,#f3f3f5 40%,#e6a3aa 60%,#eef0f2)" role="img" aria-label="Glossy red lip gloss tubes on a light grey background"></div>
    <div class="cat-name">Glossy Finish</div>
    <div class="btn-line cat-btn">Shop Now</div>
  </div>
  <div class="abs card" style="left:139px;top:656px;height:108px">
    <div class="card-photo" style="height:68px;background:linear-gradient(135deg,#9c3b40,#f2f0f0 40%,#efeded 55%,#d88a9c 80%)" role="img" aria-label="Black lipsticks beside chocolates and pink satin"></div>
    <div class="cat-name">Matte Finish</div>
    <div class="btn-line cat-btn">Shop Now</div>
  </div>
  <div class="abs card" style="left:228px;top:656px;height:108px">
    <div class="card-photo" style="height:68px;background:linear-gradient(135deg,#ecebea,#ffffff 45%,#6d6d6d 70%,#e8e6e6)" role="img" aria-label="White and black cosmetic tubes with boxes"></div>
    <div class="cat-name">Plumping Gloss</div>
    <div class="btn-line cat-btn">Shop Now</div>
  </div>
  <div class="abs card" style="left:317px;top:656px;height:108px">
    <div class="card-photo" style="height:68px;background:linear-gradient(135deg,#9c3b40,#f2f0f0 40%,#efeded 55%,#d88a9c 80%)" role="img" aria-label="Lip oil tubes beside chocolates and pink satin"></div>
    <div class="cat-name">Lip Oil</div>
    <div class="btn-line cat-btn">Shop Now</div>
  </div>

  <h2 class="abs section-title" style="left:0;top:808px;font-size:12.5px">Best Sellers</h2>
  <div class="abs rule" style="left:200px;top:829px;width:27px"></div>
  <p class="abs section-sub" style="left:0;top:838px;font-size:4.5px">Our most loved lip glosses, loved by thousands of customers</p>

  <div class="abs card" style="left:50px;top:861px;height:133px">
    <div class="card-photo" style="height:75px;background:linear-gradient(90deg,#e9e9ec,#f3f3f5 40%,#e6a3aa 60%,#eef0f2)" role="img" aria-label="Crystal Shine lip gloss in red"></div>
    <div class="abs tag">Bestseller</div>
    <div class="prod-name">Crystal Shine Lip Gloss</div>
    <div class="prod-price">$24.99<s>$34.99</s></div>
    <div class="swatches"><i style="background:#ee6d95"></i><i style="background:#f3a2bb"></i><i style="background:#f7c1d0"></i><i style="background:#f7c1d0"></i></div>
    <div class="btn-solid add-btn">Add to Cart</div>
  </div>
  <div class="abs card" style="left:139px;top:861px;height:133px">
    <div class="card-photo" style="height:75px;background:linear-gradient(135deg,#f2d7bb,#efceb0 55%,#e9c2a4)" role="img" aria-label="Velvet Matte lip gloss with brushes on peach backdrop"></div>
    <div class="abs tag">Sale</div>
    <div class="prod-name">Velvet Matte Lip Gloss</div>
    <div class="prod-price">$26.99<s>$36.99</s></div>
    <div class="swatches"><i style="background:#ee6d95"></i><i style="background:#e8383f"></i><i style="background:#f08a24"></i></div>
    <div class="btn-solid add-btn">Add to Cart</div>
  </div>
  <div class="abs card" style="left:228px;top:858px;height:136px">
    <div class="card-photo" style="height:78px;background:linear-gradient(135deg,#9c3b40,#f2f0f0 40%,#efeded 55%,#d88a9c 80%)" role="img" aria-label="Hydrating Glow lip oil beside chocolates and pink satin"></div>
    <div class="prod-name">Hydrating Glow Lip Oil</div>
    <div class="prod-price">$22.99</div>
    <div class="swatches"><i style="background:#ee6d95"></i><i style="background:#f3a2bb"></i><i style="background:#f7c1d0"></i></div>
    <div class="btn-solid add-btn">Add to Cart</div>
  </div>
  <div class="abs card" style="left:317px;top:861px;height:133px">
    <div class="card-photo" style="height:75px;background:linear-gradient(135deg,#ecebea,#ffffff 45%,#6d6d6d 70%,#e8e6e6)" role="img" aria-label="Plumping lip gloss tube with box"></div>
    <div class="abs tag">New</div>
    <div class="prod-name">Plumping Lip Gloss</div>
    <div class="prod-price">$28.99</div>
    <div class="swatches"><i style="background:#ee6d95"></i><i style="background:#f7c1d0"></i><i style="background:#f3a2bb"></i></div>
    <div class="btn-solid add-btn">Add to Cart</div>
  </div>
</main>

<!-- Community page -->
<main class="page page-community">
  <section class="abs reviews"></section>
  <h2 class="abs section-title" style="left:0;top:17px;font-size:12.5px">What Our Customers Say</h2>
  <div class="abs rule" style="left:200px;top:37px;width:27px"></div>
  <p class="abs section-sub" style="left:0;top:45px;font-size:4.5px">Real reviews from real customers</p>

  <article class="abs review" style="left:40px">
    <div class="abs avatar" style="background:#e9b49f" role="img" aria-label="Customer portrait"></div>
    <div class="abs rev-name">Amelia Brooks</div>
    <div class="abs stars">★★★★★</div>
    <p class="abs quote">"The Crystal Shine Lip Gloss is absolutely amazing! It gives my lips the perfect shine without feeling sticky. I get compliments every time I wear it. Will definitely repurchase!"</p>
  </article>
  <article class="abs review" style="left:158px">
    <div class="abs avatar" style="background:#7a5a4c" role="img" aria-label="Customer portrait"></div>
    <div class="abs rev-name">Lena Ortiz</div>
    <div class="abs stars">★★★★★</div>
    <p class="abs quote">"As someone with darker skin, it's hard to find lip glosses that show up well. Glow With Mirela's shades are perfect and the formula is so hydrating! The plumping gloss is my favorite."</p>
  </article>
  <article class="abs review" style="left:277px">
    <div class="abs avatar" style="background:#3b2e2a" role="img" aria-label="Customer portrait"></div>
    <div class="abs rev-name">Hana Kim</div>
    <div class="abs stars">★★★★☆</div>
    <p class="abs quote">"I love that Glow With Mirela is cruelty-free and uses sustainable packaging. The products are amazing and I feel good about supporting an ethical brand. The lip oils are especially nourishing."</p>
  </article>

  <h2 class="abs section-title" style="left:0;top:186px;font-size:12.5px">Follow Us on Instagram</h2>
  <div class="abs rule" style="left:200px;top:205px;width:27px"></div>
  <p class="abs section-sub" style="left:0;top:213px;font-size:4.5px">Tag @glowwithmirela for a chance to be featured</p>
  <div class="abs insta-tile" style="left:40px;background:linear-gradient(135deg,#f2d7bb,#e9c2a4)" role="img" aria-label="Makeup flat lay on peach"></div>
  <div class="abs insta-tile" style="left:99px;background:linear-gradient(90deg,#e9e9ec,#e6a3aa 55%,#eef0f2)" role="img" aria-label="Red lip gloss tubes"></div>
  <div class="abs insta-tile" style="left:158px;background:linear-gradient(135deg,#f4b3bf,#f2d2c6 60%,#e9b7a6)" role="img" aria-label="Model wearing red gloss"></div>
  <div class="abs insta-tile" style="left:216px;background:linear-gradient(135deg,#ecebea,#fff 45%,#6d6d6d 72%,#e8e6e6)" role="img" aria-label="Cosmetic tubes and boxes"></div>
  <div class="abs insta-tile" style="left:276px;background:linear-gradient(135deg,#f4b3bf,#f2d2c6 60%,#e9b7a6)" role="img" aria-label="Model wearing red gloss"></div>
  <div class="abs insta-tile" style="left:335px;background:linear-gradient(135deg,#f4b3bf,#f2d2c6 60%,#e9b7a6)" role="img" aria-label="Model wearing red gloss"></div>

  <section class="abs newsletter"></section>
  <h3 class="abs news-title">Join Our Beauty Community</h3>
  <p class="abs news-copy">Subscribe to our newsletter and be the first to know about new<br>products, exclusive offers, and beauty tips.</p>
  <div class="abs news-input"><span>Your email address</span><b>Subscribe</b></div>

  <footer class="abs footer">
    <div class="abs foot-head" style="left:40px">Glow With Mirela</div>
    <div class="abs foot-rule" style="left:40px"></div>
    <p class="abs foot-about">Premium lip glosses crafted with care to enhance your natural beauty and nourish your lips.</p>
    <div class="abs social" style="left:40px"></div>
    <div class="abs social" style="left:55px"></div>
    <div class="abs social" style="left:70px"></div>
    <div class="abs social" style="left:85px"></div>

    <div class="abs foot-head" style="left:130px">Shop</div>
    <div class="abs foot-rule" style="left:130px"></div>
    <ul class="abs foot-list" style="left:130px"><li>All Products</li><li>Best Sellers</li><li>New Arrivals</li><li>Sale</li><li>Gift Cards</li></ul>

    <div class="abs foot-head" style="left:219px">Help</div>
    <div class="abs foot-rule" style="left:219px"></div>
    <ul class="abs foot-list" style="left:219px"><li>Contact Us</li><li>Shipping &amp; Returns</li><li>FAQs</li><li>Privacy Policy</li><li>Terms of Service</li></ul>

    <div class="abs foot-head" style="left:309px">Contact</div>
    <div class="abs foot-rule" style="left:309px"></div>
    <ul class="abs foot-list" style="left:309px">
      <li><svg viewBox="0 0 10 10"><rect x="0.5" y="2" width="9" height="6.5" fill="#fff"/><path d="M0.5 2 L5 5.5 L9.5 2" stroke="#2b2b2b" fill="none"/></svg>hello@glowwithmirela.com</li>
      <li><svg viewBox="0 0 10 10"><path d="M2 1 L4 1 L4.8 3.3 L3.6 4.3 C4.3 5.7 5 6.4 6.2 7 L7.2 5.8 L9.4 6.6 L9.4 8.6 C9.4 9.2 8.8 9.6 8.2 9.5 C4.5 9 1.4 5.9 1 2.2 C1 1.5 1.4 1 2 1 Z" fill="#fff"/></svg>+1 (555) 010-2288</li>
      <li><svg viewBox="0 0 10 10"><path d="M5 0.5 C2.8 0.5 1.4 2.1 1.4 4 C1.4 6.5 5 9.8 5 9.8 C5 9.8 8.6 6.5 8.6 4 C8.6 2.1 7.2 0.5 5 0.5 Z" fill="#fff"/><circle cx="5" cy="4" r="1.3" fill="#2b2b2b"/></svg>48 Rose Lane, Bloom City</li>
    </ul>
  </footer>
</main>

</body>
</html>
```